Keen Volt Electrical in need of a business card design

We need a new business card designed for our electrical business. We have a logo already which I will attach below.
Would like the business card to be..
-BLACK background preferably, possibly white back ground behind logo if colours clash.
-White & Blue (logo blue) text
Something that makes the logo pop, & a modern look. Possibly minimal clean format.

REQUIRE:
-Logo on front & back

TEXT TO INCLUDE (ON ONE SIDE):

Tom Harlow
Director/Electrician
M: 0412 563 718
E:info@keenvoltelectrical.com.au
W:www.keenvoltelectrical.com.au
R.E.C 58431

Custom/New Homes
Renovations
Commercial Office/Shop Fit-outs
Communications & Security Cameras
Electric Vehicle Chargers
Airconditioning
Updates

Requirements
Nice to have
• Possibly even lighten the grey shades for the words 'Keen' & 'Volt' to be more easily read on a black background.

```html
<!DOCTYPE html>
<html lang="en">
<head>
<meta charset="utf-8">
<title>Keen Volt Electrical – Business Card</title>
<link rel="stylesheet" href="https://fonts.googleapis.com/css2?family=Quicksand:wght@500;600;700&family=Montserrat:wght@600;700&display=swap">
<style>
  :root {
    --page-bg: #dcdcdc;
    --card-dark: #1d2731;
    --card-mid: #323e49;
    --card-light: #5d6a75;
    --brand-blue: #0f9ad8;
    --brand-blue-bright: #14b6ec;
    --text-white: #f2f5f8;
    --text-soft: #d5dde4;
  }
  * { margin: 0; padding: 0; box-sizing: border-box; }
  html, body { width: 1200px; height: 1200px; overflow: hidden; }
  body {
    background: var(--page-bg);
    font-family: "Quicksand", "Helvetica Neue", Arial, sans-serif;
    position: relative;
  }
  .card {
    position: absolute;
    left: 262px;
    width: 686px;
    height: 392px;
    border-radius: 26px;
    overflow: hidden;
    background: linear-gradient(20deg, var(--card-dark) 0%, var(--card-mid) 55%, var(--card-light) 100%);
  }
  .card--front { top: 165px; }
  .card--back { top: 653px; }

  /* Front */
  .person {
    position: absolute;
    right: calc(686px - 298px);
    top: 166px;
    text-align: right;
  }
  .person__name {
    font-family: "Montserrat", "Helvetica Neue", Arial, sans-serif;
    font-weight: 700;
    font-size: 30px;
    line-height: 1;
    color: var(--brand-blue);
    letter-spacing: 0.2px;
  }
  .person__role {
    font-weight: 500;
    font-size: 15.5px;
    color: var(--text-white);
    margin-top: 1px;
  }
  .divider {
    position: absolute;
    left: 320px;
    top: 163px;
    width: 1.5px;
    height: 56px;
    background: var(--brand-blue);
  }
  .contact {
    position: absolute;
    left: 339px;
    top: 160px;
    list-style: none;
    font-weight: 500;
    font-size: 15.5px;
    line-height: 19.5px;
    color: var(--text-white);
  }
  .web-band {
    position: absolute;
    left: 69px;
    right: 0;
    top: 317px;
    height: 34px;
    background: linear-gradient(90deg, var(--brand-blue) 0%, var(--brand-blue-bright) 100%);
  }
  .web-band__url {
    position: absolute;
    left: 0;
    right: 0;
    top: 0;
    line-height: 34px;
    text-align: center;
    padding-right: 60px;
    font-size: 14.5px;
    font-weight: 500;
    letter-spacing: 4px;
    color: var(--text-white);
  }
  .web-band__url strong { font-weight: 700; }
  .brand-square-small {
    position: absolute;
    left: 32px;
    top: 322px;
    width: 24px;
    height: 24px;
    background: var(--brand-blue);
  }

  /* Back */
  .brand {
    position: absolute;
    left: 0;
    right: 0;
    top: 160px;
    display: flex;
    align-items: center;
    justify-content: center;
    gap: 18px;
  }
  .brand__mark {
    width: 44px;
    height: 44px;
    background: var(--brand-blue);
  }
  .brand__name {
    font-family: "Montserrat", "Helvetica Neue", Arial, sans-serif;
    font-weight: 600;
    font-size: 44px;
    line-height: 1;
    color: var(--text-soft);
    letter-spacing: 0.5px;
  }
  .services {
    position: absolute;
    left: 0;
    right: 0;
    top: 314px;
    text-align: center;
    font-weight: 500;
    font-size: 15.5px;
    line-height: 19px;
    color: var(--text-soft);
  }
  .services__sep {
    display: inline-block;
    width: 4px;
    height: 4px;
    margin: 0 4px 3px;
    background: var(--brand-blue-bright);
    vertical-align: middle;
  }
</style>
</head>
<body>
  <section class="card card--front" aria-label="Business card front">
    <div class="person">
      <div class="person__name">TOM HARLOW</div>
      <div class="person__role">Director/Electrician</div>
    </div>
    <div class="divider"></div>
    <ul class="contact">
      <li>0412 563 718</li>
      <li>info@keenvoltelectrical.com.au</li>
      <li>R.E.C 58431</li>
    </ul>
    <div class="brand-square-small"></div>
    <div class="web-band">
      <div class="web-band__url">www.<strong>KeenVoltElectrical</strong>.com.au</div>
    </div>
  </section>

  <section class="card card--back" aria-label="Business card back">
    <div class="brand">
      <div class="brand__mark"></div>
      <div class="brand__name">Keen Volt Electrical</div>
    </div>
    <div class="services">
      <div>Custom/New Homes<span class="services__sep"></span>Renovations<span class="services__sep"></span>Commercial Office/Shop Fit-outs</div>
      <div>Communications &amp; Security Cameras<span class="services__sep"></span>Electric Vehicle Chargers<span class="services__sep"></span>Airconditioning</div>
    </div>
  </section>
</body>
</html>
```